Business Card Design for Venture Kite

Venture Kite is a pro bono student consultancy service offered by Corvala KTRB to social start ups and enterprises. We provide consulting services with expertise in areas such as Marketing, IT, Business Strategy and Innovation.
I have attached\ the Venture Kite Logo here for your perusal.
Industry/Entity Type
Business
Contact Information for Business Card
Name: Ha Min Park Name: Thomas Leung
Role: Project Leader Role: Vice Project Leader
M:0477203941 M: 0479352806
E: ha-min.park@corvalaktrb.org E: thomas.leung@corvalaktrb.org
W: www.corvalaktrb.org W: www.corvalaktrb.org

```html
<!DOCTYPE html>
<html lang="en">
<head>
<meta charset="utf-8">
<title>Venture Kite — Business Cards</title>
<link rel="stylesheet" href="https://fonts.googleapis.com/css2?family=Mulish:wght@400;600;800&display=swap">
<style>
  :root {
    --backdrop: #ececec;
    --front-top: #8b8e93;
    --front-bottom: #585a61;
    --accent-gold: #f2b630;
    --logo-cream: #f7f1e3;
    --card-white: #ffffff;
    --ink: #1d1d1f;
    --ink-soft: #3a3a3d;
    --rule-grey: #77797e;
    --icon-grey: #b9bcc2;
  }
  * { box-sizing: border-box; margin: 0; padding: 0; }
  html, body {
    width: 1200px;
    height: 720px;
    overflow: hidden;
    background: var(--backdrop);
    font-family: "Mulish", sans-serif;
  }
  .canvas {
    position: relative;
    width: 1200px;
    height: 720px;
  }
  .card {
    position: absolute;
    top: 97px;
    width: 300px;
    height: 525px;
  }
  .card--front {
    left: 246px;
    background: linear-gradient(180deg, var(--front-top) 0%, var(--front-bottom) 100%);
  }
  .card--back {
    left: 653px;
    background: var(--card-white);
    text-align: center;
  }
  .gold-rule {
    position: absolute;
    left: 19px;
    right: 19px;
    height: 3px;
    background: var(--accent-gold);
  }
  .gold-rule--top { top: 18px; }
  .gold-rule--bottom { bottom: 15px; }

  .wordmark {
    font-weight: 800;
    text-transform: uppercase;
    line-height: 1;
    letter-spacing: 0.01em;
  }
  .card--front .wordmark {
    position: absolute;
    left: 0;
    right: 0;
    top: 208px;
    text-align: center;
    color: var(--logo-cream);
    font-size: 44px;
  }
  .card--back .wordmark {
    margin-top: 110px;
    color: var(--ink);
    font-size: 28px;
  }

  .holder-name {
    margin-top: 52px;
    font-size: 17px;
    font-weight: 600;
    color: var(--ink-soft);
    text-transform: uppercase;
  }
  .holder-role {
    margin-top: 4px;
    font-size: 9px;
    font-weight: 600;
    color: var(--ink-soft);
    text-transform: uppercase;
  }
  .contact-list {
    margin-top: 20px;
    list-style: none;
    font-size: 13px;
    font-weight: 600;
    color: var(--ink);
    line-height: 17px;
  }
  .contact-label { font-size: 10px; }
  .divider {
    width: 42px;
    height: 2px;
    margin: 12px auto 0;
    background: var(--rule-grey);
  }
  .social-row {
    position: absolute;
    left: 0;
    right: 0;
    top: 450px;
    display: flex;
    justify-content: center;
    gap: 7px;
  }
  .social-slot {
    width: 25px;
    height: 25px;
    border-radius: 3px;
    background: var(--icon-grey);
  }
</style>
</head>
<body>
  <main class="canvas">
    <section class="card card--front" aria-label="Card front">
      <div class="gold-rule gold-rule--top"></div>
      <h1 class="wordmark">Venture<br>Kite</h1>
      <div class="gold-rule gold-rule--bottom"></div>
    </section>

    <section class="card card--back" aria-label="Card back">
      <h2 class="wordmark">Venture<br>Kite</h2>
      <p class="holder-name">Thomas Leung</p>
      <p class="holder-role">Vice Project Leader</p>
      <ul class="contact-list">
        <li><span class="contact-label">M:</span> 0479352806</li>
        <li>thomas.leung@corvalaktrb.org</li>
        <li>www.corvalaktrb.org</li>
      </ul>
      <div class="divider"></div>
      <div class="social-row">
        <span class="social-slot" role="img" aria-label="Social network link"></span>
        <span class="social-slot" role="img" aria-label="Social network link"></span>
        <span class="social-slot" role="img" aria-label="Social network link"></span>
      </div>
    </section>
  </main>
</body>
</html>
```